Business Card Design

Velvet Pixel Promotions

An online marketing consulting & strategy business for the cosmetic niche

We specialise in Increasing Leads, Conversions & Content Marketing

I am looking for a very clean, BOLD business card that is simple & effective

Target Market(s)

cosmetic surgeons & cosmetic clinics

Industry/Entity Type

Marketing

Contact Information for Business Card

Darren Okoye
Online Marketing Strategist

Darren@VelvetPixelPromotions.example
0491 268 517

LinkedIn: in/darrenokoye

```html
<!DOCTYPE html>
<html lang="en">
<head>
<meta charset="utf-8">
<title>Velvet Pixel Promotions – Business Card</title>
<link href="https://fonts.googleapis.com/css2?family=Jura:wght@500&family=Roboto:wght@400;500&display=swap" rel="stylesheet">
<style>
  :root {
    --backdrop: #ebe8e3;
    --teal: #2e8c86;
    --mid-green: #4fab62;
    --lime: #8cc63e;
    --deep-green: #0e3a18;
    --band-green: #13491f;
    --ink-light: #e4e6e3;
    --ink-white: #f4f5f2;
  }
  * { box-sizing: border-box; margin: 0; padding: 0; }
  html, body {
    width: 1200px; height: 723px; overflow: hidden;
    background: var(--backdrop);
  }
  .stage {
    position: relative; width: 1200px; height: 723px;
  }
  .card {
    position: absolute; top: 207px;
    width: 540px; height: 309px;
    overflow: hidden;
    box-shadow: 0 6px 18px rgba(0,0,0,.18);
  }
  /* Reverse side */
  .card-back {
    left: 40px;
    background: linear-gradient(35deg, var(--teal) 0%, var(--mid-green) 55%, var(--lime) 100%);
    display: flex; align-items: center; justify-content: center;
  }
  .back-mark {
    display: flex; align-items: center; gap: 14px;
    font-family: "Jura", sans-serif; font-weight: 500;
    color: var(--ink-light);
  }
  .back-mark .mark-dot {
    width: 56px; height: 56px; border-radius: 50%;
    border: 7px solid var(--ink-light);
  }
  .back-mark .mark-name {
    display: flex; flex-direction: column;
    font-size: 15px; line-height: 1.1; letter-spacing: 2px; text-transform: uppercase;
  }
  .back-mark .mark-name .wide { letter-spacing: 7.2px; }

  /* Front side */
  .card-front { left: 620px; background: var(--mid-green); }
  .facet-field {
    position: absolute; inset: 0 0 74px 0;
    background:
      linear-gradient(120deg, rgba(255,255,255,.08) 0 30%, transparent 30% 60%, rgba(0,0,0,.06) 60%),
      linear-gradient(25deg, #1f9a66 0%, #3daa55 50%, #6fbd3f 100%);
  }
  .wordmark {
    position: absolute; left: 34px; top: 40px;
    display: flex; align-items: center; gap: 20px;
    font-family: "Jura", sans-serif; font-weight: 500;
    color: var(--ink-light);
  }
  .wordmark .mark-dot {
    width: 96px; height: 96px; border-radius: 50%;
    border: 12px solid var(--ink-light);
  }
  .wordmark .mark-name {
    display: flex; flex-direction: column;
    font-size: 38px; line-height: 1.02; text-transform: uppercase; letter-spacing: 2px;
  }
  .wordmark .mark-name .wide { letter-spacing: 19.5px; }
  .contact-band {
    position: absolute; left: 0; right: 0; bottom: 0; height: 74px;
    background: linear-gradient(90deg, var(--deep-green), var(--band-green));
    display: flex; justify-content: space-between; align-items: center;
    padding: 0 26px;
    font-family: "Roboto", sans-serif; color: var(--ink-white);
  }
  .contact-col { display: flex; flex-direction: column; gap: 8px; }
  .contact-line { display: flex; align-items: center; gap: 8px; font-size: 13px; }
  .contact-line svg { width: 20px; height: 20px; flex: none; }
  .role-line { font-size: 11px; letter-spacing: .4px; padding-left: 28px; }
  .role-line strong { font-weight: 500; }
</style>
</head>
<body>
<main class="stage">
  <section class="card card-back" aria-label="Business card reverse">
    <div class="back-mark">
      <span class="mark-dot"></span>
      <span class="mark-name"><span>Velvet</span><span class="wide">Pixel</span><span>Promotions</span></span>
    </div>
  </section>

  <section class="card card-front" aria-label="Business card front">
    <div class="facet-field" role="img" aria-label="Faceted green geometric background"></div>
    <div class="wordmark">
      <span class="mark-dot"></span>
      <span class="mark-name"><span>Velvet</span><span class="wide">Pixel</span><span>Promotions</span></span>
    </div>
    <div class="contact-band">
      <div class="contact-col">
        <div class="contact-line">
          <svg viewBox="0 0 20 20" aria-hidden="true"><circle cx="10" cy="10" r="9" fill="none" stroke="currentColor" stroke-width="1.4"/><path d="M7 5.5l1.8 2.2-1 1.2c.6 1.3 1.6 2.3 2.9 2.9l1.2-1 2.2 1.8-1 1.6c-3.6-.4-6.6-3.4-7-7z" fill="currentColor"/></svg>
          <span>0491 268 517</span>
        </div>
        <div class="contact-line">
          <svg viewBox="0 0 20 20" aria-hidden="true"><circle cx="10" cy="10" r="9" fill="none" stroke="currentColor" stroke-width="1.4"/></svg>
          <span>in/darrenokoye</span>
        </div>
      </div>
      <div class="contact-col">
        <div class="contact-line">
          <svg viewBox="0 0 20 20" aria-hidden="true"><circle cx="10" cy="10" r="9" fill="none" stroke="currentColor" stroke-width="1.4"/><rect x="5" y="6.5" width="10" height="7" fill="none" stroke="currentColor" stroke-width="1.2"/><path d="M5 6.5l5 4 5-4" fill="none" stroke="currentColor" stroke-width="1.2"/></svg>
          <span>Darren@VelvetPixelPromotions.example</span>
        </div>
        <div class="role-line"><strong>Darren Okoye</strong> Online Marketing Strategist</div>
      </div>
    </div>
  </section>
</main>
</body>
</html>
```